A3 Event Poster for School Fundraiser

We are looking for a bold, engaging, and professional A3 poster design to promote a special school fundraising event. A top athlete will be visiting a primary school to inspire children, encourage participation in sport, and help launch a fundraising initiative to raise money for new PE/sports equipment for the school.

The poster will be displayed prominently outside the school and shared with parents and families. Its purpose is to generate excitement, explain the event quickly, and encourage parents/families to sponsor and get involved.

We work with about 50 different athletes so will need the design to be easy to alter the picture of the athlete/name etc so it can be replicated across the different athletes.

Target Market(s)

Priamary School Parents/Communities

Industry/Entity Type

Education

Font styles to use
Other font styles liked:
• The logo font is Rajdhani. ‘Corvel’ is bold, ‘Pennix’ is semibold and the strapline is regular.

Requirements
Must have
• Space for the Event Date (that school can write in themselves), A picture of the visiting athlete and their bio (with ability to easily change)
Nice to have
• Bold, eye-catching

```html
<!DOCTYPE html>
<html lang="en">
<head>
<meta charset="utf-8">
<title>Inspirational Athlete Visiting Our School</title>
<link rel="stylesheet" href="https://fonts.googleapis.com/css2?family=Oswald:wght@400;500;600&family=Rajdhani:wght@400;600;700&family=Roboto:wght@400;700&family=Montserrat:ital,wght@1,800&family=Permanent+Marker&display=swap">
<style>
  :root {
    --purple: #7a3c8c;
    --purple-deep: #5a2a86;
    --navy: #16142f;
    --orange: #f5a91b;
    --gold: #f2b417;
    --red: #d4213d;
    --grey: #7a7a7a;
    --white: #ffffff;
    --charcoal: #2a2a2c;
    --ink: #111111;
  }
  * { margin: 0; padding: 0; box-sizing: border-box; }
  html, body { width: 851px; height: 1200px; overflow: hidden; background: var(--white); }
  .poster {
    position: relative;
    width: 851px;
    height: 1200px;
    overflow: hidden;
    background:
      linear-gradient(180deg, rgba(22,20,47,0) 60%, rgba(22,20,47,0.85) 88%, var(--navy) 100%),
      radial-gradient(ellipse 420px 520px at 130px 780px, #3b3aa0 0%, rgba(90,42,134,0.85) 45%, rgba(255,255,255,0) 100%),
      radial-gradient(ellipse 360px 500px at 820px 560px, rgba(246,140,150,0.55) 0%, rgba(255,255,255,0) 100%),
      linear-gradient(160deg, #ffffff 0%, #f8f4fa 40%, #e9def0 100%);
  }
  .side-band {
    position: absolute;
    left: 42px; top: 0;
    width: 111px; height: 652px;
  }
  .side-band__word {
    font-family: "Oswald", sans-serif;
    font-weight: 400;
    font-size: 92px;
    fill: var(--white);
  }
  .brand {
    position: absolute;
    left: 536px; top: 34px;
    display: flex; flex-direction: column;
    font-family: "Rajdhani", sans-serif;
  }
  .brand__row { display: flex; align-items: center; gap: 8px; }
  .brand__dot { width: 24px; height: 24px; border-radius: 50%; background: var(--purple); }
  .brand__name { font-weight: 700; font-size: 40px; line-height: 1; color: var(--purple); }
  .brand__strap { font-weight: 400; font-size: 12px; color: var(--purple); margin-left: 32px; }
  .court-art {
    position: absolute;
    left: 173px; top: 81px;
    width: 369px; height: 163px;
    background: linear-gradient(90deg, #f7b42a, var(--orange));
    border-radius: 6px;
  }
  .heart-mark {
    position: absolute;
    left: 766px; top: 115px;
    width: 58px; height: 84px;
    background: rgba(245,169,27,0.35);
    border-radius: 29px;
  }
  .mission {
    position: absolute;
    right: 44px; top: 175px;
    width: 290px;
    text-align: right;
    font-family: "Roboto", sans-serif;
    font-weight: 700;
    font-size: 15px;
    line-height: 20.5px;
    color: var(--grey);
  }
  .hero-photo {
    position: absolute;
    left: 500px; top: 252px;
    width: 351px; height: 948px;
    background:
      radial-gradient(circle at 140px 150px, #e8c9b4 0%, rgba(232,201,180,0) 38%),
      radial-gradient(circle at 170px 540px, #f4c21c 0%, #2c3d9c 28%, rgba(44,61,156,0) 40%),
      linear-gradient(180deg, #c49a78 0%, #e23a47 45%, #df2a3c 100%);
    border-radius: 160px 160px 0 0;
  }
  .headline {
    position: absolute;
    left: 170px; top: 270px;
    width: 350px; height: 262px;
  }
  .headline__text {
    font-family: "Oswald", sans-serif;
    font-weight: 600;
    fill: var(--purple);
    text-transform: uppercase;
  }
  .role {
    position: absolute;
    left: 210px; top: 535px;
    width: 222px; height: 152px;
  }
  .role__text {
    font-family: "Permanent Marker", "Oswald", sans-serif;
    font-size: 42px;
    fill: var(--white);
  }
  .athlete-photo {
    position: absolute;
    left: 13px; top: 658px;
    width: 166px; height: 166px;
    border-radius: 50%;
    border: 7px solid var(--orange);
    background: linear-gradient(160deg, #e8eaf2 0%, #5b6fb0 60%, #1c2a6a 100%);
    z-index: 2;
  }
  .bio {
    position: absolute;
    left: 173px; top: 706px;
    width: 267px; height: 88px;
    background: var(--orange);
    padding: 8px 8px 0 19px;
    font-family: "Roboto", sans-serif;
    font-size: 12.6px;
    line-height: 14.6px;
    color: var(--ink);
    white-space: nowrap;
  }
  .scribble { position: absolute; left: 178px; top: 798px; }
  .cause {
    position: absolute;
    left: 64px; top: 926px;
    transform: translate(-50%, -50%) rotate(-90deg);
    width: 124px;
    font-family: "Roboto", sans-serif;
    font-size: 11px;
    line-height: 13px;
    color: var(--white);
    white-space: nowrap;
  }
  .slogans {
    position: absolute;
    left: 94px; top: 862px;
    font-family: "Montserrat", sans-serif;
    font-style: italic;
    font-weight: 800;
    font-size: 30px;
    line-height: 41px;
    text-transform: uppercase;
    white-space: nowrap;
  }
  .slogans__line--gold { color: var(--gold); margin-left: 4px; }
  .slogans__line--red { color: var(--red); }
  .slogans__line--purple { color: #8a4fb0; }
  .slogan-rings { position: absolute; left: 140px; top: 864px; }
  .date-box {
    position: absolute;
    left: 38px; top: 1037px;
    width: 313px; height: 88px;
    background: var(--charcoal);
    display: flex; align-items: center; justify-content: center;
    padding-top: 20px;
    font-family: "Oswald", sans-serif;
    font-weight: 500;
    font-size: 30px;
    color: var(--gold);
    text-transform: uppercase;
  }
</style>
</head>
<body>
<main class="poster">
  <svg class="side-band" viewBox="0 0 111 652" aria-label="Inspirational">
    <rect width="111" height="652" fill="var(--purple)"/>
    <text class="side-band__word" transform="translate(93 626) rotate(-90)" textLength="584" lengthAdjust="spacingAndGlyphs">INSPIRATIONAL</text>
  </svg>

  <div class="brand">
    <div class="brand__row"><span class="brand__dot"></span><span class="brand__name">CorvelPennix</span></div>
    <span class="brand__strap">Inspiring every child</span>
  </div>

  <div class="court-art" role="img" aria-label="Orange brushstroke with a volleyball court outline and a volleyball"></div>
  <div class="heart-mark" role="img" aria-label="Orange hand-drawn heart decoration"></div>

  <p class="mission">INSPIRING EVERY CHILD TO LEAD<br>AN ACTIVE, RESILIENT AND<br>HEALTHY LIFE</p>

  <div class="hero-photo" role="img" aria-label="Photo of a young pupil in a red sports top holding a yellow and blue volleyball"></div>

  <h1>
    <svg class="headline" viewBox="0 0 350 262" aria-label="Athlete visiting our school">
      <text class="headline__text" x="3" y="91" font-size="108" textLength="336" lengthAdjust="spacingAndGlyphs">ATHLETE</text>
      <text class="headline__text" x="10" y="186" font-size="108" textLength="331" lengthAdjust="spacingAndGlyphs">VISITING</text>
      <text class="headline__text" x="10" y="254" font-size="63" textLength="292" lengthAdjust="spacingAndGlyphs">OUR SCHOOL</text>
    </svg>
  </h1>

  <svg class="role" viewBox="0 0 222 152" aria-label="Olympic volleyball player">
    <text class="role__text" x="40" y="44" textLength="138" lengthAdjust="spacingAndGlyphs">OLYMPIC</text>
    <text class="role__text" x="13" y="94" textLength="196" lengthAdjust="spacingAndGlyphs">VOLLEYBALL</text>
    <text class="role__text" x="47" y="146" textLength="131" lengthAdjust="spacingAndGlyphs">PLAYER</text>
  </svg>

  <div class="athlete-photo" role="img" aria-label="Portrait photo of the visiting athlete in team kit"></div>
  <p class="bio">Daniel is a dynamic English<br>volleyball player and coach, known<br>for his leadership on and off the<br>court and his passion for inspiring<br>the next generation through sport.</p>

  <svg class="scribble" width="90" height="40" viewBox="0 0 90 40" aria-hidden="true">
    <path d="M8 26 C30 30 40 10 52 18 C60 24 48 30 44 22 C42 14 70 8 86 6" fill="none" stroke="#fff" stroke-width="2.5" stroke-linecap="round"/>
    <path d="M16 20 L6 27 L16 32" fill="none" stroke="#fff" stroke-width="2.5" stroke-linecap="round" stroke-linejoin="round"/>
  </svg>

  <p class="cause">Help us raise<br>funds for new<br>sports equipment</p>

  <svg class="slogan-rings" width="320" height="120" viewBox="0 0 320 120" aria-hidden="true">
    <ellipse cx="110" cy="20" rx="100" ry="15" fill="none" stroke="#fff" stroke-opacity="0.7" stroke-width="1.2"/>
    <ellipse cx="185" cy="61" rx="132" ry="18" fill="none" stroke="#fff" stroke-opacity="0.7" stroke-width="1.2"/>
    <ellipse cx="95" cy="102" rx="92" ry="15" fill="none" stroke="#fff" stroke-opacity="0.7" stroke-width="1.2"/>
  </svg>
  <div class="slogans">
    <div class="slogans__line--gold">Be Inspired</div>
    <div class="slogans__line--red">Make a Difference</div>
    <div class="slogans__line--purple">Get Active</div>
  </div>

  <div class="date-box">Event Date Space</div>
</main>
</body>
</html>
```